Facebook cover photo and profile picture for local trade construction quotation website

Hi,I need a Facebook design for a cover photo and profile picture ,to meet the new facebook design branding requirements which are:
Background cover photo image : 851 x 315 px JPEG
Profile picture : high quality image that scales well from 180 x 180 pixels to 32 x 32 pixels JPEG
The Facebook page is for my new website which is a trade quatation site, you can visit the website at www.tradebidly.je to get a feel for the website. We would like the profile picture to be the name of the website ( tradebidly.je) and to be in Orange and black as it is on the website, this will be in the centre of the picture feel free to have any colour background or add anything around the writing I am open to any ideas .
For the background cover photo, I am again open to any design idea , perhaps it should have a cartoon builder which you can use from the website homepage and have that somewhere in the design , and possibly have the website address www.tradebidly.je and perhaps the email address which is enquiries@tradebidly.je other than that please feel free to use your imagination I am looking for the WOW factor to attract people to the website.

```html
<!DOCTYPE html>
<html lang="en">
<head>
<meta charset="utf-8">
<title>tradebidly.je — Cover</title>
<link rel="stylesheet" href="https://fonts.googleapis.com/css2?family=Source+Sans+3:wght@400;700&display=swap">
<style>
  :root {
    --ink: #3d2b26;
    --cream-deep: #fce8b6;
    --cream-light: #fdf2d9;
    --photo-light: #f4f4f4;
    --photo-mid: #e2e2e2;
    --photo-dark: #cfcfcf;
  }
  html, body {
    margin: 0;
    padding: 0;
    overflow: hidden;
    background: #ffffff;
  }
  .cover {
    position: relative;
    width: 1200px;
    height: 444px;
    overflow: hidden;
    font-family: "Source Sans 3", "Source Sans Pro", sans-serif;
  }
  .cover__photo {
    position: absolute;
    inset: 0;
    background:
      radial-gradient(ellipse 70% 60% at 55% 0%, var(--photo-dark) 0%, transparent 70%),
      linear-gradient(110deg, var(--photo-mid) 0%, var(--photo-light) 55%, var(--photo-mid) 80%, var(--photo-light) 100%);
  }
  .cover__band {
    position: absolute;
    inset: 0;
    width: 1200px;
    height: 444px;
  }
  .cover__brand {
    position: absolute;
    left: 0;
    right: 0;
    top: 150px;
    text-align: center;
    color: var(--ink);
  }
  .brand-name {
    margin: 0;
    font-size: 76px;
    font-weight: 700;
    line-height: 1;
    letter-spacing: 1px;
  }
  .brand-email {
    margin: 22px 0 0;
    font-size: 28px;
    font-weight: 400;
    line-height: 1;
  }
</style>
</head>
<body>
  <main class="cover">
    <div class="cover__photo" role="img" aria-label="Bright photograph of a modern arched steel-and-glass roof structure, softly faded"></div>
    <svg class="cover__band" viewBox="0 0 1200 444" aria-hidden="true">
      <defs>
        <linearGradient id="creamFade" x1="0" y1="0" x2="1" y2="0">
          <stop offset="0" stop-color="var(--cream-deep)"/>
          <stop offset="1" stop-color="var(--cream-light)"/>
        </linearGradient>
      </defs>
      <polygon points="0,96 1175,444 0,444" fill="url(#creamFade)"/>
    </svg>
    <div class="cover__brand">
      <h1 class="brand-name">tradebidly.je</h1>
      <p class="brand-email">enquiries@tradebidly.je</p>
    </div>
  </main>
</body>
</html>
```